Front and back cover design for skincare marketing materials

Thank you for showing an interest in my project.
Project Details.

I require a front and back cover for our marketing materials.
·       Front Cover size: 105 mm W x 150 mm H.
·       Back Cover size:  105 mm W x 150 mm H.
·       It must include these two colors. You can use a third color if you wish.
1.     #DBA09D
2.     #FFFFFF
 
Front Cover
·      The front cover will have a faded image of the Kakadu Plum branch and fruit. There are two image files, KP_image-1.jpg and kp_image-2.jpeg. You can use both images, just a portion of them, or source alternative royalty-free images of Kakadu Plum that may better fit the design. These two files have been uploaded.
 
The front cover wording.
Top of the front cover.
a.     The title of the image. “Kakadu Plum”
b.     The brand name, “Velora Skincare”. The file brand_name.ai uploaded.
 
Bottom of the front cover- Designer's choice of font.
The bottom of the front cover contains three lines of text in the following order.  
1.     Australian Native Ingredients
2.     100% Natural · Organic · Wild-harvested
3.     Australian-Made Premium Skincare
 
Back Cover
·      Back Cover wording.The back cover contains the following words "grown by nature" in white (#FFFFFF) of font Italianno (font_file.ttf) with a background color of #DBA09D as seen in the sample box (sample_box.pdf) right-side panel
 
Please provide one file for the front cover and a separate file for the back cover.
All the elements of the files must be editable.
 
Do NOT use the Curve function on the files, as the text must remain editable/changeable.
 
All assets/resources/files, including fonts not supplied by us but used by the designer, must be named and provided with the finished design.
Updates

Slow to provide project details.

Target Market(s)

Beauty-minded Asian consumers between the ages of 32 and 75 who take a proactive approach to maintaining younger-looking skin. Those who already know the danger of skin damage caused by skincare containing harsh chemicals choose effective natural/organic solutions to meet their skincare needs. Those who wish a more radiant glow and youthful appearance to their skin. Usually, a two-income middle to high-income bracket couples with a mindset for health and beauty.

Industry/Entity Type

beauty

Font styles to use
Other font styles liked:
• I will provide a font file and a brand name file.

Requirements
Must have
• You must use the two colors provided on the product box. The designer may use a third color.
Nice to have
• some gold colour

```html
<!DOCTYPE html>
<html lang="en">
<head>
<meta charset="UTF-8">
<title>Velora Skincare – Kakadu Plum Covers</title>
<link href="https://fonts.googleapis.com/css2?family=Italianno&family=Barlow+Condensed:wght@300&display=swap" rel="stylesheet">
<style>
  :root {
    --brand-pink: #dba09d;
    --paper-white: #ffffff;
    --ink-grey: #4a4a4a;
    --copy-grey: #5a5a5a;
    --stage: #ececec;
    --leaf-dark: #3f8a2e;
    --leaf-light: #9ccc4a;
    --fruit-glow: #e0823a;
  }
  * { margin: 0; padding: 0; box-sizing: border-box; }
  html, body {
    width: 1200px;
    height: 848px;
    overflow: hidden;
    background: var(--stage);
  }
  .cover-spread {
    position: absolute;
    left: 40px;
    top: 24px;
    width: 1120px;
    height: 800px;
    display: flex;
  }
  .cover {
    width: 560px;
    height: 800px;
    position: relative;
  }
  .back-cover {
    background: var(--brand-pink);
  }
  .back-cover .tagline {
    position: absolute;
    left: 0;
    width: 100%;
    top: 440px;
    text-align: center;
    font-family: "Italianno", cursive;
    font-size: 82px;
    line-height: 1;
    color: var(--paper-white);
  }
  .front-cover {
    background: var(--paper-white);
  }
  .brand-name {
    position: absolute;
    left: 0;
    width: 100%;
    top: 150px;
    text-align: center;
    font-family: "Barlow Condensed", sans-serif;
    font-weight: 300;
    font-size: 46px;
    letter-spacing: 0.12em;
    text-transform: uppercase;
    color: var(--brand-pink);
  }
  .product-title {
    position: absolute;
    left: 0;
    width: 100%;
    top: 250px;
    text-align: center;
    font-family: "Italianno", cursive;
    font-size: 78px;
    line-height: 1;
    color: var(--ink-grey);
  }
  .botanical-art {
    position: absolute;
    left: 130px;
    top: 330px;
    width: 310px;
    height: 320px;
  }
  .ingredient-lines {
    position: absolute;
    left: 0;
    width: 100%;
    top: 668px;
    text-align: center;
    font-family: "Barlow Condensed", sans-serif;
    font-weight: 300;
    font-size: 24px;
    line-height: 34px;
    color: var(--copy-grey);
    list-style: none;
  }
</style>
</head>
<body>
  <main class="cover-spread">
    <section class="cover back-cover">
      <p class="tagline">Grown By Nature</p>
    </section>
    <section class="cover front-cover">
      <p class="brand-name">Velora Skincare</p>
      <h1 class="product-title">Kakadu Plum</h1>
      <svg class="botanical-art" viewBox="0 0 310 320" role="img" aria-label="Painted illustration of a Kakadu plum branch with green leaves and ripening fruit">
        <defs>
          <radialGradient id="branch-tones" cx="55%" cy="50%" r="60%">
            <stop offset="0%" stop-color="var(--leaf-light)"/>
            <stop offset="55%" stop-color="var(--leaf-dark)" stop-opacity="0.75"/>
            <stop offset="100%" stop-color="var(--paper-white)" stop-opacity="0"/>
          </radialGradient>
        </defs>
        <rect width="310" height="320" fill="url(#branch-tones)"/>
      </svg>
      <ul class="ingredient-lines">
        <li>Australian Native Ingredients</li>
        <li>100% Natural · Organic · Wild-harvested</li>
        <li>Australian-Made Premium Skincare</li>
      </ul>
    </section>
  </main>
</body>
</html>
```